New Website for NY and South Florida Based Accounting Firm

Accounting and Audit firm located in New York and South Florida needs a website redesign after acquiring new businesses and adding new services.

Our current website can be found here:
http://www.trqbnllp.example/

We have merged with this firm:
http://hollisbarkerwendtfield.example/

We are looking for a comprehensive design that will highlight the firm's dual locations. The final design should communicate security, strength, and growth. We would like to keep our pyramid logo as seen on the trqbnllp.example website, as this has been our logo for over 20 years.

Industry/Entity Type

Accounting

Number of Pages Required

1 page

Font styles to use
Serif
Sans Serif

```html
<!DOCTYPE html>
<html lang="en">
<head>
<meta charset="utf-8">
<title>TRQBN — Tax, Audit and Business Advisory</title>
<link rel="stylesheet" href="https://fonts.googleapis.com/css2?family=Raleway:wght@500;600;700&family=Open+Sans:wght@400;600;700&display=swap">
<style>
:root{
  --orange:#f4a95b;
  --orange-dark:#e8923a;
  --ink:#2b2b2b;
  --text:#444;
  --muted:#777;
  --white:#fff;
  --dark:#2a2d35;
  --nav:#333;
  --grey:#c9c9c9;
  --wall:#d6d1c9;
  --suit:#1f2640;
  --paper:#f4f4f3;
}
*{margin:0;padding:0;box-sizing:border-box}
html,body{width:1200px;height:2683px;overflow:hidden;background:var(--white)}
body{position:relative;font-family:"Open Sans",Arial,sans-serif;color:var(--text)}
.abs{position:absolute}

/* header */
.site-header{left:0;top:0;width:1200px;height:111px;background:var(--white)}
.brand{left:50px;top:22px;display:flex;flex-direction:column;align-items:center;gap:8px}
.brand-mark{width:34px;height:34px;background:var(--orange)}
.brand-name{font-family:"Open Sans",sans-serif;font-weight:600;font-size:21px;color:var(--ink);letter-spacing:1px}
.social{left:794px;top:12px;display:flex;gap:9px}
.social span{width:18px;height:18px;border-radius:3px;background:#666;display:block}
.search{left:1132px;top:12px}
.main-nav{left:520px;top:70px;display:flex}
.main-nav a{font-size:13px;font-weight:600;color:var(--nav);text-decoration:none;letter-spacing:.3px;padding:0 17px;position:relative;height:41px}
.main-nav a.active::after{content:"";position:absolute;left:8px;right:8px;bottom:0;height:4px;background:var(--orange)}

/* hero */
.hero{left:0;top:111px;width:1200px;height:520px;
  background:linear-gradient(90deg,#cbc6be 0%,#ddd8d1 12%,#cfc9c1 20%,#2b3250 26%,#1c2338 34%,#e6e6e8 42%,#f6f6f6 47%,#202740 53%,#1a2034 60%,#eeeeee 66%,#fbfbfb 76%,#e9e9e9 86%,#c6c4c0 93%,#a9a7a3 100%)}
.hero-caption{left:0;top:438px;width:1200px;height:82px;background:rgba(30,30,30,.72)}
.hero-caption p{position:absolute;left:48px;top:12px;width:960px;font-family:"Raleway",sans-serif;font-weight:500;font-size:24px;line-height:28px;color:var(--white)}
.dots{left:1052px;top:496px;display:flex;gap:6px}
.dots i{width:11px;height:11px;border-radius:50%;background:#bbb;display:block}
.dots i.on{background:var(--orange)}

/* why */
.section-title{width:1200px;left:0;text-align:center;font-family:"Raleway",sans-serif;font-weight:700;font-size:33px;color:var(--ink);letter-spacing:1px}
.tabs{left:86px;top:764px;width:1026px;display:flex;justify-content:space-between}
.tab{font-family:"Raleway",sans-serif;font-weight:500;font-size:20px;color:var(--ink);padding-bottom:8px;border-bottom:4px solid var(--ink);text-align:center}
.tab.active{border-color:var(--orange)}
.why-text{left:100px;top:832px;width:1000px;text-align:center;font-size:15px;line-height:18px;color:var(--text)}
.why-text p+p{margin-top:18px}

/* testimonial */
.testimonial{left:0;top:1057px;width:1200px;height:438px;
  background:linear-gradient(90deg,#26272b 0%,#3d3b3b 15%,#55514d 30%,#4a4644 45%,#6a625b 58%,#4b4848 72%,#37383e 86%,#23252b 100%)}
.avatar{left:556px;top:1120px;width:89px;height:89px;border-radius:50%;background:linear-gradient(#d9a27e,#8a5040);border:3px solid var(--white)}
.quote-name{left:0;top:1220px;width:1200px;text-align:center;font-weight:700;font-size:15px;color:var(--white)}
.quote-text{left:145px;top:1258px;width:910px;text-align:center;font-size:16px;line-height:23px;color:var(--white)}

/* people */
.portrait{border:4px solid #ddd}
.person-role{left:386px;top:1866px;font-family:"Raleway",sans-serif;font-size:15px;color:var(--ink)}
.person-contact{left:386px;top:1903px;font-size:11px;font-weight:700;line-height:17px;color:var(--ink)}

/* services */
.services{left:0;top:1994px;width:1200px;height:506px;
  background:linear-gradient(115deg,#1c222c 0%,#2f3644 25%,#4a5162 45%,#3a4252 62%,#262c38 80%,#171b23 100%)}
.services .section-title{color:var(--white);top:50px}
.service{width:260px;text-align:center;top:2160px}
.service-icon{width:114px;height:114px;border:2px solid var(--white);border-radius:50%;margin:0 auto;display:flex;align-items:center;justify-content:center}
.service h3{margin-top:34px;font-family:"Raleway",sans-serif;font-weight:700;font-size:16px;color:var(--orange);letter-spacing:.5px}
.service p{margin:18px auto 0;width:215px;font-family:Arial,sans-serif;font-size:13px;line-height:19px;color:var(--white)}

/* footer */
.site-footer{left:0;top:2500px;width:1200px;height:183px;background:var(--orange)}
.footer-brand{left:86px;top:2552px;display:flex;align-items:center;gap:10px}
.footer-brand .brand-mark{width:22px;height:22px;background:#4a3b2a}
.footer-brand span{font-weight:600;font-size:18px;color:#4a3b2a}
.copyright{left:76px;top:2610px;font-family:Arial,sans-serif;font-size:13px;line-height:22px;color:var(--white)}
.footer-links{list-style:none;font-family:Arial,sans-serif;font-size:15px;line-height:28.5px;color:var(--white)}
.footer-links li::before{content:"";display:inline-block;border-left:6px solid var(--white);border-top:4px solid transparent;border-bottom:4px solid transparent;margin-right:14px;vertical-align:1px}
.map{left:665px;top:2519px;width:140px;height:140px;border-radius:50%;border:5px solid var(--white);background:linear-gradient(135deg,#ece9e2,#d3cec3)}
.office{left:837px;top:2527px;font-family:Arial,sans-serif;color:var(--white)}
.office h4{font-size:15px;font-weight:700}
.office p{margin-top:22px;font-size:15px;line-height:22px}
</style>
</head>
<body>

<header class="site-header abs">
  <div class="brand abs"><span class="brand-mark"></span><span class="brand-name">TRQBN</span></div>
  <div class="social abs" aria-hidden="true"><span></span><span></span><span></span><span></span><span></span><span></span><span></span><span></span><span></span><span></span><span></span></div>
  <svg class="search abs" width="18" height="18" viewBox="0 0 18 18" aria-label="Search"><circle cx="7.5" cy="7.5" r="5.5" fill="none" stroke="#333" stroke-width="2"/><line x1="11.5" y1="11.5" x2="16" y2="16" stroke="#333" stroke-width="2.4"/></svg>
  <nav class="main-nav abs">
    <a class="active">HOME</a><a>WHY TRQBN</a><a>SERVICES</a><a>PROFILES</a><a>TIPS &amp; LINKS</a><a>CONTACT</a>
  </nav>
</header>

<section class="hero abs" role="img" aria-label="Photo of a smiling businesswoman in a navy pinstripe suit holding up a white sheet of paper in a bright office">
  <div class="hero-caption abs"><p>TRQBN is a tax, audit and business advisory practice with over 30 professionals in NYC and Long Island.</p></div>
  <div class="dots abs"><i class="on"></i><i></i><i></i></div>
</section>
<svg class="abs" style="left:22px;top:336px" width="40" height="72" viewBox="0 0 40 72"><polyline points="36,2 4,36 36,70" fill="none" stroke="#fff" stroke-width="4"/></svg>
<svg class="abs" style="left:1136px;top:336px" width="40" height="72" viewBox="0 0 40 72"><polyline points="4,2 36,36 4,70" fill="none" stroke="#fff" stroke-width="4"/></svg>

<h2 class="section-title abs" style="top:664px">WHY TRQBN?</h2>
<div class="tabs abs">
  <span class="tab" style="width:164px">THE RESOURCES</span>
  <span class="tab active" style="width:130px">THE PEOPLE</span>
  <span class="tab" style="width:158px">THE EXPERTISE</span>
  <span class="tab" style="width:336px">INNOVATION. INTEGRITY. RESULTS.</span>
</div>
<div class="why-text abs">
  <p>TORRANCE, REILLY, QUINN, BRANDT &amp; NOLAN, LLP is a progressive accounting and business management firm with offices in New York City, Long Island, and Florida. We offer experience, financial solutions and vast resources in all aspects of accounting, tax planning, tax return preparation, personal financial planning, estate and trust, and small business consulting, all backed by a commitment to one-on-one attention and an unwavering dedication to meeting the highest business standards.</p>
  <p>Since our founding in 1984, we have built our reputation on our ability to provide timely, quality service and assistance that surpasses our clients’ expectations. In the face of increasingly complex regulations and financial options, our staff is able to present winning solutions.</p>
</div>

<section class="testimonial abs" role="img" aria-label="Dimmed photo of colleagues smiling around a laptop in a meeting"></section>
<div class="avatar abs" role="img" aria-label="Client portrait"></div>
<p class="quote-name abs">Clara Vendell, USA</p>
<p class="quote-text abs">TORRANCE, REILLY, QUINN, BRANDT &amp; NOLAN, LLP is a progressive accounting and business management firm with offices in New York City, Long Island, and Florida. We offer experience, financial solutions and vast resources in all aspects of accounting, tax planning, tax return preparation, personal financial planning, estate and trust, and small business consulting, all backed by a commitment to one-on-one attention and an unwavering dedication to meeting the highest business standards.</p>

<h2 class="section-title abs" style="top:1542px">OUR PEOPLE</h2>
<svg class="abs" style="left:52px;top:1722px" width="22" height="40" viewBox="0 0 22 40"><polyline points="20,2 3,20 20,38" fill="none" stroke="#333" stroke-width="2.5"/></svg>
<svg class="abs" style="left:1138px;top:1722px" width="22" height="40" viewBox="0 0 22 40"><polyline points="2,2 19,20 2,38" fill="none" stroke="#333" stroke-width="2.5"/></svg>
<div class="portrait abs" style="left:110px;top:1652px;width:161px;height:176px;background:linear-gradient(90deg,#b9b5b0 0%,#8a6446 22%,#d8ab8c 42%,#e4bba0 55%,#7d5638 78%,#2a2626 100%)" role="img" aria-label="Portrait of a female team member with long brown hair in a dark blazer"></div>
<div class="portrait abs" style="left:387px;top:1625px;width:211px;height:225px;background:linear-gradient(160deg,#2f2a27 0%,#8a6a55 30%,#c79a7e 48%,#4a4d5e 68%,#1f2230 100%)" role="img" aria-label="Portrait of a thoughtful male partner in a suit holding glasses"></div>
<div class="portrait abs" style="left:679px;top:1655px;width:163px;height:173px;background:linear-gradient(90deg,#f2f1ef 0%,#e3e1de 35%,#c49a80 55%,#5a4036 72%,#9a9ba3 88%,#d8d7d5 100%)" role="img" aria-label="Portrait of a female team member holding a tablet"></div>
<div class="portrait abs" style="left:942px;top:1651px;width:163px;height:173px;background:linear-gradient(180deg,#7a7b80 0%,#c8a28c 30%,#1e1f26 55%,#2e5fa8 68%,#1a1b22 82%,#c0342e 100%)" role="img" aria-label="Portrait of a senior male partner in a black robe holding a red book"></div>
<p class="person-role abs">National Guild of Accountants</p>
<p class="person-contact abs">SUPPORT@BRIGHTLEDGER.EXAMPLE<br>TEL: 800-555-0142</p>

<section class="services abs" role="img" aria-label="Dimmed photo of hands typing on a keyboard">
  <h2 class="section-title abs">OUR SERVICES</h2>
</section>
<div class="service abs" style="left:49px">
  <div class="service-icon"><svg width="40" height="40" viewBox="0 0 40 40"><g stroke="#fff" stroke-width="4" stroke-linecap="round"><line x1="8" y1="32" x2="30" y2="10"/><line x1="10" y1="10" x2="32" y2="32"/></g><circle cx="31" cy="9" r="5" fill="none" stroke="#fff" stroke-width="3"/></svg></div>
  <h3>ACCOUNTING &amp; AUDITING</h3>
  <p>Lorem ipsum dolor sit amet, consectetur adipiscing elit, sed do eiusmod tempor incididunt ut labore et magna.</p>
</div>
<div class="service abs" style="left:333px">
  <div class="service-icon"><svg width="40" height="44" viewBox="0 0 40 44"><g fill="none" stroke="#fff" stroke-width="2.5"><rect x="6" y="12" width="16" height="30"/><rect x="22" y="4" width="12" height="38"/></g><g fill="#fff"><rect x="10" y="17" width="3" height="3"/><rect x="15" y="17" width="3" height="3"/><rect x="10" y="24" width="3" height="3"/><rect x="15" y="24" width="3" height="3"/><rect x="10" y="31" width="3" height="3"/><rect x="15" y="31" width="3" height="3"/><rect x="26" y="10" width="4" height="3"/><rect x="26" y="18" width="4" height="3"/><rect x="26" y="26" width="4" height="3"/></g></svg></div>
  <h3>TAX SERVICES</h3>
  <p>Lorem ipsum dolor sit amet, consectetur adipiscing elit, sed do eiusmod tempor incididunt ut labore et magna.</p>
</div>
<div class="service abs" style="left:617px">
  <div class="service-icon"><svg width="40" height="40" viewBox="0 0 40 40"><polygon points="36,4 4,18 20,20 22,36" fill="#fff"/></svg></div>
  <h3>MANAGEMENT CONSULTING</h3>
  <p>Lorem ipsum dolor sit amet, consectetur adipiscing elit, sed do eiusmod tempor incididunt ut labore et magna.</p>
</div>
<div class="service abs" style="left:905px">
  <div class="service-icon"><svg width="46" height="40" viewBox="0 0 46 40"><g fill="none" stroke="#fff" stroke-width="2.5" stroke-linejoin="round"><path d="M12 10h28v18h-6v6l-6-6H12z"/><path d="M12 20H6V4h26v6"/></g></svg></div>
  <h3>FINANCIAL PLANNING</h3>
  <p>Lorem ipsum dolor sit amet, consectetur adipiscing elit, sed do eiusmod tempor incididunt ut labore et magna.</p>
</div>

<footer class="site-footer abs"></footer>
<div class="footer-brand abs"><span class="brand-mark"></span><span>TRQBN</span></div>
<p class="copyright abs">Copyright 2015.<br>All Rights Reserved.</p>
<ul class="footer-links abs" style="left:286px;top:2538px"><li>Home</li><li>About Us</li><li>Services</li><li>Why Choose Us</li></ul>
<ul class="footer-links abs" style="left:477px;top:2540px"><li>Blog Page</li><li>FAQ</li><li>Pricing</li><li>Contact</li></ul>
<div class="map abs" role="img" aria-label="Street map of the New York City office location">
  <svg class="abs" style="left:53px;top:28px" width="24" height="34" viewBox="0 0 24 34"><path d="M12 33C4 21 1 16 1 11a11 11 0 0 1 22 0c0 5-3 10-11 22z" fill="#d94a3a"/><circle cx="12" cy="11" r="4" fill="#fff"/></svg>
</div>
<div class="office abs">
  <h4>New York City Office</h4>
  <p>220 Harbor Avenue 2nd Floor<br>New York, NY 10010<br>Phone: (631) 555-0178</p>
</div>

</body>
</html>
```